The homepage of a website

This is a simple project that should take from you a few minutes as what is needed is the design of the homepage only, the details are in the attached zip file

Please note that KBLTA board required a special tailored design where they got some parts from the different posted designs, if you are interested please follow the instructions in the below URL and submit your new updated designs as per the instructions (P.S. I will mark the project as guaranteed as an assurance to all of you)

http://quorvanet.com/Projects/KBLTA/Design.jpg

Please note that KBLTA board required a special tailored design where they got some parts from the different posted designs, if you are interested please follow the instructions in the below URL and submit your new updated designs as per the instructions (P.S. I will mark the project as guaranteed as an assurance to all of you) http://quorvanet.com/Projects/KBLTA/Design.jpg

```html
<!DOCTYPE html>
<html lang="en">
<head>
<meta charset="utf-8">
<title>KBLTA – Home</title>
<link href="https://fonts.googleapis.com/css2?family=Libre+Franklin:wght@400;700;900&family=Roboto+Condensed:wght@700&family=Arimo:wght@400;700&display=swap" rel="stylesheet">
<style>
:root{
  --navy:#2f4268;
  --navy-dark:#2a3c62;
  --nav-top:#61769e;
  --nav-bottom:#354a70;
  --gold:#e2c97f;
  --gold-line:#d9be6c;
  --gold-band:#d6bb6a;
  --orange:#f26522;
  --text:#1f1f1f;
  --muted:#555;
  --panel:#fff;
  --card-grey:#ebebeb;
  --footer-ink:#5b4f2c;
}
*{box-sizing:border-box;margin:0;padding:0}
html,body{width:1099px;height:1200px;overflow:hidden;background:#fff}
body{position:relative;font-family:"Arimo",Arial,sans-serif;color:var(--text)}
.abs{position:absolute}
.hero{left:133px;top:0;width:845px;height:570px;
  background:radial-gradient(ellipse at 30% 55%,#fbf8cf 0%,#eef2a8 30%,#cfe08a 55%,rgba(255,255,255,0) 80%),
  linear-gradient(90deg,#a7cf5a 0%,#e4ef9e 25%,#f7f3d2 55%,#e9d8c8 80%,#d9b9a3 100%);}
.hero-fade{left:133px;top:430px;width:845px;height:140px;background:linear-gradient(rgba(255,255,255,0),#fff)}
.header{left:163px;top:0;width:785px;height:157px;background:linear-gradient(#fff,#f1f1f1);border-radius:0 0 8px 8px;box-shadow:0 2px 6px rgba(0,0,0,.25)}
.brand{left:188px;top:18px;display:flex;align-items:center;gap:10px}
.brand-mark{width:34px;height:34px;border-radius:50%;background:var(--navy)}
.brand-name{font:700 30px "Libre Franklin",sans-serif;color:var(--navy)}
.brand-full{left:470px;top:18px;width:190px;text-align:right;font:700 15px/1.35 "Libre Franklin",sans-serif;color:var(--navy-dark)}
.divider-v{left:702px;top:0;width:1px;height:100px;background:#d8d8d8}
.contact{left:745px;top:30px;font-size:11px;color:#c89a2f;line-height:19px}
.contact li{list-style:none;display:flex;align-items:center;gap:7px}
.contact svg{width:11px;height:11px}
.nav{left:173px;top:114px;width:765px;height:37px;border-radius:6px;background:linear-gradient(var(--nav-top),var(--nav-bottom));display:flex}
.nav a{color:#fff;text-decoration:none;font-size:12.5px;padding:0 20px;line-height:37px;border-right:1px solid rgba(255,255,255,.25)}
.nav a:first-child{padding-left:19px}
.search{left:767px;top:119px;width:163px;height:26px;border-radius:6px;background:#fff;box-shadow:inset 0 1px 3px rgba(0,0,0,.3)}
.search svg{position:absolute;right:6px;top:4px}
.headline{left:234px;top:283px;width:370px;border-top:2px solid #fff;border-bottom:2px solid #fff;padding:4px 0 2px;color:var(--navy)}
.headline b{display:block;font:900 33px/1.05 "Libre Franklin",sans-serif}
.headline span{display:block;font:400 32px/1.1 "Libre Franklin",sans-serif}
.dots{left:164px;top:446px;display:flex;gap:8px}
.dots i{width:11px;height:11px;border-radius:50%;background:#c5c9cf}
.dots i:first-child{background:var(--navy)}
.panel{background:var(--panel);border:1px solid #ddd;border-radius:6px;box-shadow:0 1px 4px rgba(0,0,0,.2)}
.panel-title{font:700 14px "Roboto Condensed",sans-serif;color:var(--navy);padding:0 0 2px 16px;border-bottom:1px solid var(--gold-line);margin-bottom:10px}
.education{left:163px;top:474px;width:540px;height:314px;padding:8px 16px}
.education .panel-title{width:277px}
.card{position:absolute;width:245px;height:119px;background:linear-gradient(90deg,#fff,var(--card-grey));box-shadow:0 4px 4px -2px rgba(0,0,0,.35)}
.card .photo{position:absolute;left:0;top:0;width:119px;height:119px}
.card h3{position:absolute;left:122px;top:1px;width:120px;font:700 11px/13px "Arimo",sans-serif;color:#222}
.card p{position:absolute;left:122px;top:31px;width:122px;font-size:10px;line-height:12.5px;color:#333}
.more{position:absolute;right:4px;bottom:4px;background:var(--navy);color:#fff;font-size:7.5px;padding:3px 4px}
.about{left:163px;top:804px;width:540px;height:217px;border-radius:6px;background:linear-gradient(#63779e,#33476d);color:#fff;padding:8px 16px}
.about .panel-title{color:#fff;border-color:var(--orange);width:277px}
.about p{margin:24px 8px 0 8px;font-size:11.6px;line-height:15px;text-indent:28px}
.about .more{background:var(--orange);right:13px;bottom:12px}
.side{left:715px;width:232px;padding:8px 8px}
.events{top:474px;height:231px;background:linear-gradient(#e6d08e,#d7bd6e);border:none}
.events .panel-title{border-color:#fff3c8;color:var(--navy)}
.event{display:flex;gap:6px;background:#efedee;height:43px;margin-bottom:4px;padding:6px 6px}
.event p{font-size:9.5px;line-height:9px;color:#555}
.event b{display:block;font-size:10px;color:#444;margin-top:1px}
.pubs{top:721px;height:166px}
.pubs ul{list-style:none;margin-top:-2px}
.pubs li{font:400 13px "Libre Franklin",sans-serif;color:#333;border-bottom:1px solid #bbb;padding:6px 0 3px}
.members{top:902px;height:119px}
.field{display:flex;justify-content:flex-end;align-items:center;gap:4px;font-size:12px;margin-bottom:5px}
.field span{width:115px;height:21px;border:1px solid #aaa;border-radius:5px;background:#fff}
.login-row{display:flex;justify-content:flex-end;align-items:center;gap:6px;font-size:7px;margin-top:8px}
.login-row em{font-style:normal;background:var(--orange);color:#fff;padding:4px 11px}
.footer{left:133px;top:1036px;width:845px;height:164px;background:var(--gold)}
.footer-band{left:133px;top:1159px;width:845px;height:41px;background:var(--gold-band);font-size:10.5px;color:#333;display:flex;justify-content:space-between;align-items:center;padding:0 31px}
.footer-band nav{display:flex;gap:11px}
.f-brand{left:160px;top:1080px;display:flex;align-items:center;gap:8px}
.f-brand .brand-mark{width:28px;height:28px;background:#8b7a4a}
.f-brand .brand-name{font-size:24px;color:var(--footer-ink)}
.f-full{left:296px;top:1060px;width:144px;text-align:right;font:700 13px/1.4 "Libre Franklin",sans-serif;color:var(--footer-ink)}
.f-divider{left:481px;top:1050px;width:1px;height:100px;background:#bfa75e}
.f-contact{left:523px;top:1074px;font-size:11px;line-height:19px;color:#333}
.f-contact li{list-style:none;display:flex;align-items:center;gap:8px}
.social{left:820px;top:1065px;width:130px;text-align:right}
.social h4{font:400 18px "Libre Franklin",sans-serif;color:#333;margin-bottom:9px}
.social div{display:flex;gap:8px;justify-content:flex-end}
.social i{width:24px;height:24px;border-radius:4px;background:#9a9a9a}
.social i:last-child{background:var(--orange)}
</style>
</head>
<body>
<div class="abs hero" role="img" aria-label="Hero photo: woman with closed eyes touching her cheek beside green bamboo leaves"></div>
<div class="abs hero-fade"></div>

<header class="abs header"></header>
<div class="abs brand"><span class="brand-mark"></span><span class="brand-name">KBLTA</span></div>
<div class="abs brand-full">The Kestrel Board of Lifting &amp; Tissue Aesthetics</div>
<div class="abs divider-v"></div>
<ul class="abs contact">
  <li><svg viewBox="0 0 12 12"><path d="M2 1l3 0 1 3-2 1c1 2 2 3 3 3l1-2 3 1 0 3c-6 0-10-4-9-9z" fill="#e0b54a"/></svg>500 312 648</li>
  <li><svg viewBox="0 0 12 12"><path d="M6 0a4 4 0 0 1 4 4c0 3-4 8-4 8S2 7 2 4a4 4 0 0 1 4-4z" fill="#e0b54a"/><circle cx="6" cy="4" r="1.5" fill="#fff"/></svg>Your Address goes here</li>
  <li><svg viewBox="0 0 12 12"><rect x="0" y="2" width="12" height="8" fill="#e0b54a"/><path d="M0 2l6 5 6-5" stroke="#fff" fill="none"/></svg>info@kblta.com</li>
</ul>
<nav class="abs nav"><a href="#">Home</a><a href="#">About</a><a href="#">News</a><a href="#">Newsletter</a><a href="#">Gallery</a><a href="#">Contact</a></nav>
<div class="abs search"><svg width="20" height="20" viewBox="0 0 20 20"><circle cx="12" cy="8" r="5.5" stroke="#222" stroke-width="2" fill="none"/><path d="M8 12l-6 6" stroke="#222" stroke-width="3"/></svg></div>

<h1 class="abs headline"><b>BEAUTY IS POWER,</b><span>A SMILE IS ITS SWORD</span></h1>
<div class="abs dots"><i></i><i></i><i></i><i></i></div>

<section class="abs panel education">
  <h2 class="panel-title">Patients education information</h2>
  <article class="card" style="left:16px;top:44px">
    <div class="photo" role="img" aria-label="Photo of a smiling surgeon in a white coat" style="background:linear-gradient(#6f6f6f,#c9c9c9)"></div>
    <h3>Sed blandit bibendum ligula</h3>
    <p>Duis mi dolor, euismod at massa nec, porttitor t ristique nisl. Mauris odio dolor, scelerisque vitae ultrices a, vulputate nec odio.</p>
    <span class="more">Read more</span>
  </article>
  <article class="card" style="left:277px;top:44px">
    <div class="photo" role="img" aria-label="Photo of a patient with surgical markings on the face" style="background:linear-gradient(135deg,#bfe0ea,#f0d7c8 60%,#2d8ed0)"></div>
    <h3>Sed blandit bibendum ligula</h3>
    <p>Duis mi dolor, euismod at massa nec, porttitor t ristique nisl. Mauris odio dolor, scelerisque vitae ultrices a, vulputate nec odio.</p>
    <span class="more">Read more</span>
  </article>
  <article class="card" style="left:16px;top:179px">
    <div class="photo" role="img" aria-label="Photo of medical staff using a diagnostic machine" style="background:linear-gradient(135deg,#c8ccd2,#8fb5b9 60%,#3aa5a8)"></div>
    <h3>Sed blandit bibendum ligula</h3>
    <p>Duis mi dolor, euismod at massa nec, porttitor t ristique nisl. Mauris odio dolor, scelerisque vitae ultrices a, vulputate nec odio.</p>
    <span class="more">Read more</span>
  </article>
  <article class="card" style="left:277px;top:179px">
    <div class="photo" role="img" aria-label="Photo of an operating room" style="background:linear-gradient(#8e979e,#d9dde0)"></div>
    <h3>Sed blandit bibendum ligula</h3>
    <p>Duis mi dolor, euismod at massa nec, porttitor t ristique nisl. Mauris odio dolor, scelerisque vitae ultrices a, vulputate nec odio.</p>
    <span class="more">Read more</span>
  </article>
</section>

<section class="abs about">
  <h2 class="panel-title">About</h2>
  <p>Sed blandit bibendum ligula. Duis mi dolor, euismod at massa nec, porttitor tristique nisl. Mauris odio dolor, scelerisque vitae ultrices a, vulputate nec odio. Sed eu mi blandit, blandit tortor eu, aliquet sapien. Donec accumsan bibendum est nec lobortis. Nam mauris l eo, vulputate at ornare vitae, rutrum sit amet ante. Donec vel justo id nisl feugiat sagittis. Aliquam auctor, enim vitae interdum pulvinar, metus odio varius ex, a varius odio tortor nec ante. Quisque dictum vel nulla tristique placerat. Mauris vel nibh tellus. Curabitur finibus justo est, nec tristique purus mollis id. Cras a metus lectus.</p>
  <span class="more">Read more</span>
</section>

<section class="abs panel side events">
  <h2 class="panel-title">Events</h2>
  <div class="event"><svg width="20" height="20" viewBox="0 0 20 20"><rect x="1" y="3" width="18" height="16" fill="none" stroke="#444" stroke-width="1.5"/><rect x="1" y="3" width="18" height="4" fill="#444"/><path d="M4 10h12M4 13h12M4 16h12M7 7v12M10 7v12M13 7v12" stroke="#444"/></svg><p>Aenean consequat sit amet enim mattis rutrum<b>15/01/2015</b></p></div>
  <div class="event"><svg width="20" height="20" viewBox="0 0 20 20"><rect x="1" y="3" width="18" height="16" fill="none" stroke="#444" stroke-width="1.5"/><rect x="1" y="3" width="18" height="4" fill="#444"/><path d="M4 10h12M4 13h12M4 16h12M7 7v12M10 7v12M13 7v12" stroke="#444"/></svg><p>Aenean consequat sit amet enim mattis rutrum<b>20/01/2015</b></p></div>
  <div class="event"><svg width="20" height="20" viewBox="0 0 20 20"><rect x="1" y="3" width="18" height="16" fill="none" stroke="#444" stroke-width="1.5"/><rect x="1" y="3" width="18" height="4" fill="#444"/><path d="M4 10h12M4 13h12M4 16h12M7 7v12M10 7v12M13 7v12" stroke="#444"/></svg><p>Aenean consequat sit amet enim mattis rutrum<b>22/02/2015</b></p></div>
  <div class="event"><svg width="20" height="20" viewBox="0 0 20 20"><rect x="1" y="3" width="18" height="16" fill="none" stroke="#444" stroke-width="1.5"/><rect x="1" y="3" width="18" height="4" fill="#444"/><path d="M4 10h12M4 13h12M4 16h12M7 7v12M10 7v12M13 7v12" stroke="#444"/></svg><p>Aenean consequat sit amet enim mattis rutrum<b>25/04/2015</b></p></div>
</section>

<section class="abs panel side pubs">
  <h2 class="panel-title">Publications</h2>
  <ul><li>KBLTA Journal</li><li>Research information</li><li>E-Learning information</li><li>Scientific activities</li><li>Universities</li></ul>
</section>

<section class="abs panel side members">
  <h2 class="panel-title">Members</h2>
  <div class="field">Username: <span></span></div>
  <div class="field">Password: <span></span></div>
  <div class="login-row">Forgot username or password ? <em>LOGIN</em></div>
</section>

<footer class="abs footer"></footer>
<div class="abs f-brand"><span class="brand-mark"></span><span class="brand-name">KBLTA</span></div>
<div class="abs f-full">The Kestrel Board of Lifting &amp; Tissue Aesthetics</div>
<div class="abs f-divider"></div>
<ul class="abs f-contact">
  <li><svg width="11" height="11" viewBox="0 0 12 12"><path d="M2 1l3 0 1 3-2 1c1 2 2 3 3 3l1-2 3 1 0 3c-6 0-10-4-9-9z" fill="#333"/></svg>500 312 648</li>
  <li><svg width="11" height="11" viewBox="0 0 12 12"><path d="M6 0a4 4 0 0 1 4 4c0 3-4 8-4 8S2 7 2 4a4 4 0 0 1 4-4z" fill="#333"/></svg>Your Address goes here</li>
  <li><svg width="11" height="11" viewBox="0 0 12 12"><rect x="0" y="2" width="12" height="8" fill="#333"/><path d="M0 2l6 5 6-5" stroke="#e2c97f" fill="none"/></svg>info@kblta.com</li>
</ul>
<div class="abs social"><h4>Join us on:</h4><div><i></i><i></i><i></i><i></i></div></div>
<div class="abs footer-band"><span>Copyright © 2015All rights reserved</span><nav><span>Privacy Practices</span><span>Laws &amp; Regulations</span></nav></div>
</body>
</html>
```